Business Card Design

We are a commercial real estate brokerage in San Francisco, leasing office buildings downtown.
I would like a clean, elegant look. Simple but powerful .

Industry/Entity Type

Business

Contact Information for Business Card

Colin Farrow
lic# 07281549
415.555.0172
colin@tarvo-commercial.example
tarvo-commercial.example

```html
<!DOCTYPE html>
<html lang="en">
<head>
<meta charset="utf-8">
<title>Tarvo Commercial – Business Card</title>
<link rel="stylesheet" href="https://fonts.googleapis.com/css2?family=Arimo:wght@400;700&display=swap">
<style>
  :root {
    --page-bg: #e6e7ea;
    --slate: #7f8fad;
    --slate-light: #a9b5cb;
    --card-white: #ffffff;
    --ink: #555a62;
    --icon: #6f7680;
  }
  * { margin: 0; padding: 0; box-sizing: border-box; }
  html, body {
    width: 1200px; height: 950px; overflow: hidden;
    background: var(--page-bg);
    font-family: "Arimo", Arial, sans-serif;
  }
  .sheet { position: relative; width: 1200px; height: 950px; }
  .card {
    position: absolute; left: 320px;
    width: 560px; height: 320px;
    box-shadow: 0 6px 18px rgba(0,0,0,0.12);
    overflow: hidden;
  }

  /* Back */
  .card-back { top: 120px; background: var(--slate); }
  .skyline-art {
    position: absolute; left: 200px; top: 66px;
    width: 160px; height: 110px;
    background: linear-gradient(180deg, #eef1f6 0%, #d7dde8 100%);
    border-radius: 2px;
  }
  .tagline {
    position: absolute; left: 0; right: 0; top: 204px;
    text-align: center; color: #fff;
    font-size: 14px; line-height: 1.45; letter-spacing: 0.2px;
  }

  /* Front */
  .card-front { top: 510px; background: var(--card-white); }
  .brand {
    position: absolute; left: 36px; top: 136px;
    display: flex; align-items: center; gap: 10px;
  }
  .brand-square { width: 36px; height: 36px; background: var(--slate); flex: none; }
  .brand-name {
    color: var(--slate); font-weight: 700; font-size: 20px;
    line-height: 1; white-space: nowrap;
  }

  .contact {
    position: absolute; left: 280px; top: 62px;
    color: var(--ink); font-size: 15px;
  }
  .contact-name {
    color: var(--slate); font-weight: 700; font-size: 21px; margin-bottom: 14px;
  }
  .contact-line {
    display: flex; align-items: center; gap: 9px; margin-bottom: 10px;
    white-space: nowrap;
  }
  .contact-line svg { width: 15px; height: 15px; flex: none; }

  .web-band {
    position: absolute; left: 0; bottom: 0; width: 560px; height: 62px;
  }
  .web-url {
    position: absolute; right: 22px; bottom: 12px;
    color: #fff; font-size: 16px; letter-spacing: 0.6px;
  }
</style>
</head>
<body>
<main class="sheet">

  <section class="card card-back">
    <div class="skyline-art" role="img" aria-label="Illustration of downtown office towers"></div>
    <p class="tagline">commercial real estate brokerage in San Francisco<br>leasing office buildings downtown.</p>
  </section>

  <section class="card card-front">
    <div class="brand">
      <div class="brand-square"></div>
      <p class="brand-name">Tarvo Commercial</p>
    </div>

    <div class="contact">
      <p class="contact-name">Colin Farrow</p>
      <p class="contact-line">lic# 07281549</p>
      <p class="contact-line">
        <svg viewBox="0 0 16 16" aria-hidden="true"><path fill="var(--icon)" d="M3 2h3l1.5 3.5-2 1.2a8 8 0 0 0 3.8 3.8l1.2-2L14 10v3a1 1 0 0 1-1 1A11 11 0 0 1 2 3a1 1 0 0 1 1-1z"/></svg>
        415.555.0172
      </p>
      <p class="contact-line">
        <svg viewBox="0 0 16 16" aria-hidden="true"><rect x="1.5" y="3.5" width="13" height="9" fill="var(--icon)"/><path d="M1.5 3.5 8 9l6.5-5.5" fill="none" stroke="#fff" stroke-width="1.2"/></svg>
        colin@tarvo-commercial.example
      </p>
    </div>

    <svg class="web-band" viewBox="0 0 560 62" aria-hidden="true">
      <polygon points="300,18 560,18 560,62 290,62" fill="var(--slate)"/>
      <polygon points="296,12 560,12 560,15 294,15" fill="var(--slate-light)"/>
    </svg>
    <p class="web-url">tarvo-commercial.example</p>
  </section>

</main>
</body>
</html>
```